New design for existing catalog pages

We want to update and improve our existing design. The existing products on the designs should be adopted. Also the prices, descriptions and article numbers.
It is important that we receive an Indesign file that we can adapt. Also replace the images and adjust texts and prices.

Target Market(s)

Older people with high incomes. More conservative people.

Industry/Entity Type

Münzen und Briefmarkenhandel

Requirements
Must have
• Noble, simple and timeless design that looks high quality.
Nice to have
• The expensive products should be presented accordingly
Should not have
• Don't look cheap. Not too many different and bright colors

```html
<!DOCTYPE html>
<html lang="de">
<head>
<meta charset="utf-8">
<title>Katalog – Top Münz-Raritäten</title>
<link rel="stylesheet" href="https://fonts.googleapis.com/css2?family=Lato:wght@400;700&display=swap">
<style>
:root{
  --backdrop:#727272;
  --page:#ffffff;
  --band:#c9c9c9;
  --band-dark:#b3b3b3;
  --ink:#231f20;
  --ink-soft:#3a3a3a;
  --gold-light:#f3df8a;
  --gold:#d9b33c;
  --gold-deep:#a9831d;
}
*{margin:0;padding:0;box-sizing:border-box}
html,body{width:1200px;height:2897px;overflow:hidden;background:var(--backdrop)}
body{position:relative;font-family:"Lato",sans-serif;color:var(--ink)}
.page{position:absolute;left:85px;width:1030px;height:1332px;background:var(--page);box-shadow:0 14px 18px rgba(0,0,0,.55)}
.page--one{top:92px}
.page--two{top:1474px}
.abs{position:absolute}
.catalog-title{left:61px;top:52px;font-size:26px;line-height:32px;font-weight:400;letter-spacing:.2px}
.product-band{left:0;width:466px;height:57px;background:var(--band);border-radius:0 29px 29px 0;padding:6px 0 0 63px;font-size:19px;line-height:23px}
.product-band--single{padding:15px 0 0 77px;font-size:23px}
.pill{width:198px;height:31px;background:var(--band);border-radius:16px;text-align:center;font-size:15px;line-height:31px}
.pill--sku{left:64px}
.pill--price{left:268px}
.body-copy{left:68px;width:400px;font-size:13.6px;line-height:17.4px;color:var(--ink-soft)}
.body-copy p+p{margin-top:17.4px}
.specs{left:68px;list-style:none;font-size:13.6px;line-height:17.4px;color:var(--ink-soft)}
.specs li{padding-left:22px;position:relative}
.specs li::before{content:"";position:absolute;left:2px;top:6px;width:7px;height:7px;border-radius:50%;background:var(--ink)}
.tag{font-size:23px;letter-spacing:.3px}
.coin-art{left:0;top:0;width:1030px;height:1332px;pointer-events:none}
.footer{left:0;top:0;width:1030px;height:1332px}
.footer-label{left:62px;top:1283px;font-size:16px}
.page-no{font-size:14px;left:924px;top:1261px;width:40px;text-align:center}
</style>
</head>
<body>

<section class="page page--one">
  <h1 class="abs catalog-title">DUPLONE UND DOPPELDUPLONE DER<br>Helvetischen Republik 1798 - 1803</h1>

  <h2 class="abs product-band" style="top:150px">16 FRANKEN 1800,&nbsp; Helvetische Republik -<br>DUPLONE</h2>
  <div class="abs pill pill--sku" style="top:221px">7997.1800.015</div>
  <div class="abs pill pill--price" style="top:221px">9500,– CHF</div>

  <div class="abs body-copy" style="top:279px">
    <p>Helvetische Republik ist die offizielle Bezeichnung des schweizerischen Staatswesens, das am 12. April 1798 die alte Eidgenossenschaft ablöste und bis zum 10. März 1803 bestand.</p>
    <p>Frankreich nutzte die bestehende Unzufriedenheit der ländlichen Eliten in den Untertanengebieten der alten Eidgenossenschaft, sowie der aufgeklärten Bürger in den städtischen Orten und förderte gezielt revolutionäre Bestrebungen. Angefacht oder ausgelöst und zugleich auch abgesichert wurde die Umwälzung durch französische Truppen, die ab Ende Januar in einer Zangenbewegung von der Waadt und vom Jura her in das westliche Mittelland vorstiessen (Franzoseneinfall). In den Kampfhandlungen Anfang März 1798 ging die alte Eidgenossenschaft unter.</p>
    <p>Einige Städte, allen voran Bern, hatten beträchtliche Vermögen in ihren Schatzkammern. Der sogenannte Staatsschatz von Bern wurde von den Französischen Truppen geplündert. Mehrere Kutschen mit Gold und Silber, sowie die Bären aus dem Bärengraben, wurden nach Paris gekarrt.</p>
    <p>Mit der Einführung der Helvetischen Republik ging das Münzwesen von den Kantonen auf den Zentralstaat über und der Franken wurde als Währung festgelegt. In dieser Zeit entstanden die Duplonen (16 Franken) und Doppelduplonen (32 Franken) der Helvetischen Republik.</p>
  </div>

  <ul class="abs specs" style="top:779px">
    <li>Schweiz - 16</li>
    <li>1800, Helvetische Republik</li>
    <li>23 mm Durchmesser</li>
    <li>7,65 Gramm - Gold</li>
    <li>23 mm Durchmesser</li>
    <li>vorzüglich bis unzirkuliert</li>
  </ul>

  <div class="abs tag" style="left:553px;top:523px">TOP - RARITÄT</div>

  <h2 class="abs product-band" style="top:918px;padding-left:74px">32 FRANKEN 1800, Helvetische Republik -<br>DOPPELDUPLONE</h2>
  <div class="abs pill pill--sku" style="top:989px">7997.1800.025</div>
  <div class="abs pill pill--price" style="top:989px">28900,– CHF</div>

  <ul class="abs specs" style="top:1076px">
    <li>Schweiz - 32 Franken</li>
    <li>1800, Helvetische Republik</li>
    <li>29 mm Durchmesser</li>
    <li>15,26 Gramm - Gold</li>
    <li>29 mm Durchmesser</li>
    <li>vorzüglich bis unzirkuliert</li>
  </ul>

  <div class="abs tag" style="left:551px;top:1218px">DUPLONENPAAR</div>

  <svg class="abs coin-art" viewBox="0 0 1030 1332">
    <defs>
      <radialGradient id="gold1" cx="40%" cy="35%" r="70%">
        <stop offset="0" stop-color="var(--gold-light)"/>
        <stop offset=".6" stop-color="var(--gold)"/>
        <stop offset="1" stop-color="var(--gold-deep)"/>
      </radialGradient>
    </defs>
    <circle cx="688" cy="318" r="144" fill="url(#gold1)" role="img" aria-label="Foto: 16 Franken Goldmünze 1800, Wertseite mit Eichenkranz"/>
    <circle cx="617" cy="1044" r="118" fill="url(#gold1)" role="img" aria-label="Foto: 32 Franken Goldmünze 1800, Wertseite"/>
    <circle cx="846" cy="1083" r="135" fill="url(#gold1)" stroke="#fff" stroke-width="2" role="img" aria-label="Foto: 32 Franken Goldmünze 1800, Bildseite mit Fahnenträger"/>
  </svg>

  <svg class="abs footer" viewBox="0 0 1030 1332" aria-hidden="true">
    <path d="M0 1271 H560 C580 1271 585 1292 610 1292 H1030 V1332 H0 Z" fill="var(--band)"/>
    <path d="M0 1276 H558 C578 1276 583 1297 608 1297 H1030" fill="none" stroke="#fff" stroke-width="3"/>
    <path d="M927 1332 V1246 L964 1220 V1332 Z" fill="#fff" stroke="var(--band-dark)" stroke-width="3"/>
  </svg>
  <div class="abs footer-label">Helvetische Republik - DUPLONEN</div>
  <div class="abs page-no">01</div>
</section>

<section class="page page--two">
  <h2 class="abs product-band" style="top:59px">20 Franken 1873, 3-Punkt -<br>PROBEPRÄGUNG</h2>
  <div class="abs pill pill--sku" style="top:129px">7870.1873.01</div>
  <div class="abs pill pill--price" style="top:129px">9995,– CHF</div>

  <div class="abs body-copy" style="top:193px">
    <p>1873 liess das Finanzdepartement vom bekannten Graveur Lorenz Weidmann in seiner Prägestätte in Brüssel ein Stempelpaar und 1'000 Exemplare einer neuen Eidgenössischen Goldmünze anfertigen.</p>
    <p>Der oberste der drei Punkte beinhaltete das Münzzeichen des Graveurs und stellte einen Engelskopf dar, der jedoch bei oberflächlicher Betrachtung als Punkt wahrgenommen wird.</p>
  </div>

  <ul class="abs specs" style="top:371px">
    <li>Jahr 1873</li>
    <li>Gold – 900/1'000 Feinheit</li>
    <li>Gewicht 6,451 Gramm</li>
    <li>Durchmesser 21mm</li>
    <li>Auflage: 1'000 Stück</li>
  </ul>

  <h2 class="abs product-band product-band--single" style="top:514px">Das 100 Franken Vreneli von 1925</h2>
  <div class="abs pill pill--sku" style="top:585px">7874.1925.08</div>
  <div class="abs pill pill--price" style="top:585px">25900,– CHF</div>
  <div class="abs body-copy" style="top:650px">
    <p>1925, 100 Fr. Gold-Vreneli, bis unzirkuliert, mit Stempelglanz, Top-Erhaltung, Durchmesser: 35mm, Motiv: Helvetiakopf (Vreneli), Entwurf: Felix Ulrich Lambert, Neuchâtel, Münzzeichen B, Auflage: 5'000</p>
  </div>
  <div class="abs tag" style="left:541px;top:818px">TOP - RARITÄT</div>

  <h2 class="abs product-band product-band--single" style="top:891px">Das 100 Franken Vreneli von 1925</h2>
  <div class="abs pill pill--sku" style="top:961px">7874.1925.07</div>
  <div class="abs pill pill--price" style="top:961px">25900,– CHF</div>
  <div class="abs body-copy" style="top:1029px">
    <p>1925, 100 Fr. Gold-Vreneli, fast FDC, Top-Erhaltung, Durchmesser: 35mm, Motiv: Helvetiakopf (Vreneli), Entwurf: Felix Ulrich Lambert, Neuchâtel, Münzzeichen B, Auflage: 5'000</p>
  </div>
  <div class="abs tag" style="left:541px;top:1195px">TOP - QUALITÄT</div>

  <svg class="abs coin-art" viewBox="0 0 1030 1332">
    <defs>
      <radialGradient id="gold2" cx="40%" cy="35%" r="70%">
        <stop offset="0" stop-color="var(--gold-light)"/>
        <stop offset=".6" stop-color="var(--gold)"/>
        <stop offset="1" stop-color="var(--gold-deep)"/>
      </radialGradient>
      <radialGradient id="gold3" cx="40%" cy="35%" r="70%">
        <stop offset="0" stop-color="#f7ebc4"/>
        <stop offset=".6" stop-color="#e2c983"/>
        <stop offset="1" stop-color="#bb9a4f"/>
      </radialGradient>
    </defs>
    <circle cx="622" cy="197" r="118" fill="url(#gold2)" role="img" aria-label="Foto: 20 Franken 1873, Wertseite"/>
    <circle cx="836" cy="242" r="138" fill="url(#gold2)" stroke="#fff" stroke-width="2" role="img" aria-label="Foto: 20 Franken 1873, Bildseite mit sitzender Helvetia"/>
    <circle cx="622" cy="652" r="118" fill="url(#gold3)" role="img" aria-label="Foto: 100 Franken Vreneli 1925, Wertseite"/>
    <circle cx="839" cy="697" r="140" fill="url(#gold3)" stroke="#fff" stroke-width="2" role="img" aria-label="Foto: 100 Franken Vreneli 1925, Bildseite mit Helvetiakopf"/>
    <circle cx="621" cy="1057" r="121" fill="url(#gold3)" role="img" aria-label="Foto: 100 Franken Vreneli 1925, Wertseite"/>
    <circle cx="830" cy="1080" r="140" fill="url(#gold3)" stroke="#fff" stroke-width="3" role="img" aria-label="Foto: 100 Franken Vreneli 1925, Bildseite mit Helvetiakopf"/>
  </svg>

  <svg class="abs footer" viewBox="0 0 1030 1332" aria-hidden="true">
    <path d="M0 1271 H560 C580 1271 585 1292 610 1292 H1030 V1332 H0 Z" fill="var(--band)"/>
    <path d="M0 1276 H558 C578 1276 583 1297 608 1297 H1030" fill="none" stroke="#fff" stroke-width="3"/>
    <path d="M927 1332 V1246 L964 1220 V1332 Z" fill="#fff" stroke="var(--band-dark)" stroke-width="3"/>
  </svg>
  <div class="abs footer-label" style="left:78px">Top Münz-RARITÄTEN</div>
  <div class="abs page-no">02</div>
</section>

</body>
</html>
```